Corvane

I'm looking for business cards with the logo I've attached. I don't have an specific idea in mind and open to anything. All the usual info will be involved. Name, position in company, nr, email, address

```html
<!DOCTYPE html>
<html lang="en">
<head>
<meta charset="utf-8">
<title>Corvane Designs – Business Cards</title>
<link href="https://fonts.googleapis.com/css2?family=Poppins:wght@400;500;600;700&display=swap" rel="stylesheet">
<style>
  :root {
    --stage: #2b2b2d;
    --navy: #1a2e4d;
    --gold: #efae2f;
    --paper: #ffffff;
    --ink: #1a2e4d;
  }
  * { margin: 0; padding: 0; box-sizing: border-box; }
  html, body {
    width: 1200px; height: 900px; overflow: hidden;
    background: var(--stage);
    font-family: "Poppins", sans-serif;
  }
  .sheet {
    width: 1200px; height: 900px;
    display: flex; flex-direction: column;
    align-items: center; justify-content: center; gap: 44px;
  }
  .card {
    width: 660px; height: 377px;
    border-radius: 26px;
    position: relative; overflow: hidden;
    box-shadow: 0 14px 30px rgba(0,0,0,.45);
  }
  .card--front {
    background: var(--navy);
    display: flex; align-items: center; justify-content: center;
  }
  .brand {
    display: flex; flex-direction: column; align-items: center;
    color: var(--gold); font-weight: 600; line-height: 1;
  }
  .brand__name { font-size: 58px; letter-spacing: 1px; text-transform: uppercase; }
  .brand__sub { font-size: 22px; letter-spacing: 14px; margin-top: 12px; text-transform: uppercase; padding-left: 14px; }
  .card--back {
    background: var(--paper);
    display: flex; align-items: center;
  }
  .card--back .brand { width: 330px; }
  .card--back .brand__name { font-size: 44px; }
  .card--back .brand__sub { font-size: 17px; letter-spacing: 11px; padding-left: 11px; }
  .divider { width: 2px; height: 142px; background: var(--ink); }
  .contact { padding-left: 30px; color: var(--ink); }
  .contact__name { font-size: 24px; font-weight: 700; letter-spacing: .5px; line-height: 1.1; }
  .contact__role { font-size: 15px; font-weight: 600; color: var(--gold); margin-bottom: 14px; }
  .contact__row { display: flex; align-items: flex-start; gap: 12px; font-size: 14px; font-weight: 500; line-height: 1.45; margin-bottom: 4px; }
  .contact__row svg { width: 15px; height: 15px; flex: none; margin-top: 3px; }
</style>
</head>
<body>
<main class="sheet">
  <section class="card card--front">
    <div class="brand">
      <span class="brand__name">Corvane</span>
      <span class="brand__sub">Designs</span>
    </div>
  </section>

  <section class="card card--back">
    <div class="brand">
      <span class="brand__name">Corvane</span>
      <span class="brand__sub">Designs</span>
    </div>
    <div class="divider"></div>
    <div class="contact">
      <p class="contact__name">EVAN MARLOW</p>
      <p class="contact__role">CEO/FOUNDER</p>
      <p class="contact__row">
        <svg viewBox="0 0 24 24" fill="var(--gold)" aria-hidden="true"><path d="M6.6 10.8a15.1 15.1 0 0 0 6.6 6.6l2.2-2.2a1 1 0 0 1 1-.25 11.4 11.4 0 0 0 3.6.57 1 1 0 0 1 1 1V20a1 1 0 0 1-1 1A17 17 0 0 1 3 4a1 1 0 0 1 1-1h3.5a1 1 0 0 1 1 1c0 1.25.2 2.45.57 3.6a1 1 0 0 1-.25 1z"/></svg>
        <span>555-302-4817</span>
      </p>
      <p class="contact__row">
        <svg viewBox="0 0 24 24" fill="var(--gold)" aria-hidden="true"><path d="M2 5h20v14H2z M2 5l10 8 10-8" stroke="#fff" stroke-width="1.5"/></svg>
        <span>evan@corvanemail.com</span>
      </p>
      <p class="contact__row">
        <svg viewBox="0 0 24 24" fill="var(--gold)" aria-hidden="true"><path d="M12 2a7 7 0 0 0-7 7c0 5 7 13 7 13s7-8 7-13a7 7 0 0 0-7-7zm0 9.5A2.5 2.5 0 1 1 12 6.5a2.5 2.5 0 0 1 0 5z"/></svg>
        <span>118 Alder Street NW<br>Suite 210, Fenwick Falls<br>MI 40217</span>
      </p>
    </div>
  </section>
</main>
</body>
</html>
```